ZoVEX App logo & homescreen design

We are creating a new app call "ZoVEX" that is designed for young adults (15-24 years old) to create a sexual risk reduction plan to help young adults follow their relationship goals while also being safe. Currently, we need graphic design for the ZoVEX: (1) app logo and (2) a home screen for the app. We would like to see designs that are appealing to the target population - young adults ages 15-24. These requests are only the beginning of a series of graphic designs needs that I have to develop the app - and will offer one-on-one graphic design opportunities (much more $$$ to come) for the right graphic designer. The ZoVEX app is complimentary follow-up to another commercial app we have call KALDRO, designed for doctors to assess young adults' level of sexual risk during a dr. appointment (see vantrolibsoft.com for more details) after leaving a doctors visit. I have uploaded our company branding guidelines, but am open to any colors, fonts that are appealing to the target population.

Target Market(s)

youth 15-24 years of age

Industry/Entity Type

Health And Wellness

Colors

Designer to choose colors to be used in the design.

Requirements
Must have
• Both MUST be appealing to the target market.
• The app logo should be an icon or image that represents a plan.
• The homescreen UI needs to be easy to navigate and include 4 key sections: (1) Info - this section will include educational information tailored to their sexual risk level, (2) Plan - this section will link them to create their sexual risk reduction plan, (3) Sharing - this section will link them to areas that allow them to share their plan with their doctor or others, and (4) tip - this section may be a link OR the main part of the homescreen that shares daily/weekly tips on how to stick to their plan. I suggest getting inspiration from https://www.brindelfolio.com/30-recent-inspirational-ui-examples-in-mobile-device-screens.html.
Nice to have
• In app design focus groups, youth in the target market suggested that it would should have a similar look and feel to fizzlor because they LOVE that app.
Should not have
• imply its a sexual related or healthcare/wellness related - want to to seem fun & easy to use. I open to any ideas here and am looking for YOU to be CREATIVE!!!

```html
<!DOCTYPE html>
<html lang="en">
<head>
<meta charset="utf-8">
<title>ZoVEX – App Logo &amp; Home Screen Concepts</title>
<link href="https://fonts.googleapis.com/css2?family=Questrial&display=swap" rel="stylesheet">
<style>
  :root{
    --page:#ffffff;
    --purple-top:#5400d6;
    --purple-bottom:#7c0bcf;
    --purple-ink:#6a12d2;
    --navy:#040a2a;
    --row-info:#0b2bef;
    --row-plan:#1159e0;
    --row-share:#14a0cc;
    --row-tip:#13bdc1;
    --tile-blue:#0a3ef0;
    --tile-teal:#17c8c2;
    --white:#ffffff;
    --card-shadow:0 6px 14px rgba(40,0,90,.28);
  }
  *{box-sizing:border-box;margin:0;padding:0}
  html,body{width:1200px;height:1000px;overflow:hidden;background:var(--page)}
  body{position:relative;font-family:"Questrial",sans-serif;color:var(--white)}
  .sprite{position:absolute;width:0;height:0;overflow:hidden}

  /* app icon tiles */
  .app-tile{position:absolute;top:99px;width:112px;height:112px;border-radius:26px;
    display:flex;align-items:center;justify-content:center;font-size:20px;letter-spacing:.5px;
    box-shadow:0 10px 24px rgba(60,20,140,.18)}
  .app-tile--purple{background:linear-gradient(225deg,var(--purple-top),var(--purple-bottom))}
  .app-tile--ocean{background:linear-gradient(225deg,var(--tile-teal),var(--tile-blue) 65%)}
  .tile-one{left:151px}.tile-two{left:554px}.tile-three{left:945px}

  /* home screens */
  .screen{position:absolute;top:283px;width:323px;height:574px;overflow:hidden;
    box-shadow:0 10px 30px rgba(0,0,0,.08)}
  .screen--cards{left:59px;background:linear-gradient(200deg,var(--purple-top),var(--purple-bottom))}
  .screen--bubbles{left:449px;background:linear-gradient(200deg,var(--purple-top),var(--purple-bottom))}
  .screen--rows{left:840px;background:var(--navy)}

  .status-bar{position:absolute;top:0;left:0;right:0;height:22px;display:flex;align-items:center;
    justify-content:space-between;padding:0 5px;font-family:Helvetica,Arial,sans-serif;font-size:9.5px}
  .status-left,.status-right{display:flex;align-items:center;gap:3px}
  .status-time{position:absolute;left:0;right:0;text-align:center;font-weight:600}
  .battery{width:20px;height:8px;border:1px solid var(--white);border-radius:1.5px;padding:1px}
  .battery span{display:block;width:100%;height:100%;background:var(--white)}

  .app-header{position:absolute;top:22px;left:0;right:0;height:40px;display:flex;align-items:center;justify-content:center}
  .app-title{font-size:17px;letter-spacing:.4px}
  .header-icon{position:absolute;top:11px;width:18px;height:18px;color:var(--white)}
  .header-icon--left{left:16px}.header-icon--right{right:16px}

  /* screen 1 */
  .content-card{position:absolute;left:23px;width:277px;background:var(--white);border-radius:7px;box-shadow:var(--card-shadow)}
  .card-top{top:73px;height:181px}
  .card-bottom{top:283px;height:193px}
  .tab-bar{position:absolute;left:16px;right:16px;top:500px;display:flex;justify-content:space-between}
  .tab{width:66px;display:flex;flex-direction:column;align-items:center;gap:6px;font-size:13px;opacity:.55}
  .tab--active{opacity:1}
  .tab svg{width:36px;height:36px;color:var(--white)}

  /* screen 2 */
  .bubble{position:absolute;width:98px;height:98px;border-radius:50%;background:var(--white);
    box-shadow:0 8px 16px rgba(30,0,80,.35);display:flex;align-items:center;justify-content:center;color:var(--purple-ink)}
  .bubble svg{width:38px;height:38px}
  .bubble-label{position:absolute;font-size:20px;letter-spacing:.4px}

  /* screen 3 */
  .nav-row{position:absolute;left:0;right:0;height:128px;display:flex;align-items:center}
  .nav-row svg{position:absolute;left:44px;width:38px;height:38px;color:var(--white)}
  .nav-row span{position:absolute;left:139px;font-size:20px;letter-spacing:.4px}
  .row-info{top:62px;background:var(--row-info)}
  .row-plan{top:190px;background:var(--row-plan)}
  .row-share{top:318px;background:var(--row-share)}
  .row-tip{top:446px;background:var(--row-tip)}
</style>
</head>
<body>

<svg class="sprite" aria-hidden="true">
  <symbol id="icon-info" viewBox="0 0 40 40" fill="none" stroke="currentColor" stroke-width="1.5" stroke-linecap="round">
    <circle cx="20" cy="20" r="17"/>
    <circle cx="22.5" cy="12" r="1.2" fill="currentColor" stroke="none"/>
    <path d="M18 17.5h3l-2.6 9.5q-.4 1.6 1.4 1"/>
  </symbol>
  <symbol id="icon-plan" viewBox="0 0 40 40" fill="none" stroke="currentColor" stroke-width="1.5" stroke-linecap="round">
    <path d="M3 11h34M3 20h22M3 29h26"/>
  </symbol>
  <symbol id="icon-sync" viewBox="0 0 40 40" fill="none" stroke="currentColor" stroke-width="1.5" stroke-linecap="round" stroke-linejoin="round">
    <path d="M31.5 16A12.5 12.5 0 0 0 9 12.5"/>
    <path d="M31 6.5v7.5h-7.5" transform="translate(1 1)"/>
    <path d="M8.5 24A12.5 12.5 0 0 0 31 27.5"/>
    <path d="M8 33.5V26h7.5" transform="translate(0 0)"/>
  </symbol>
  <symbol id="icon-tip" viewBox="0 0 40 40" fill="none" stroke="currentColor" stroke-width="1.5" stroke-linecap="round" stroke-linejoin="round">
    <path d="M15 24a8 8 0 1 1 10 0q-1.5 1.5-1.5 4h-7q0-2.5-1.5-4z"/>
    <path d="M17 31h6M18 34h4M19 28v-6l1 1 1-1v6"/>
    <path d="M20 4v3M10 8l2 2M30 8l-2 2M5 17h3M32 17h3"/>
  </symbol>
  <symbol id="icon-steps" viewBox="0 0 20 20" fill="none" stroke="currentColor" stroke-width="1.3" stroke-linejoin="round">
    <path d="M3 17h14V3h-5v5H8v4H3z"/><path d="M3 14.5h5"/>
  </symbol>
  <symbol id="icon-gear" viewBox="0 0 20 20" fill="none" stroke="currentColor" stroke-width="1.3" stroke-linejoin="round">
    <circle cx="10" cy="10" r="3"/>
    <path d="M8.6 2h2.8l.4 2.1 1.6.9 2-.8 1.4 2.4-1.6 1.4v1.8l1.6 1.4-1.4 2.4-2-.8-1.6.9-.4 2.3H8.6l-.4-2.3-1.6-.9-2 .8-1.4-2.4L4.8 11V9.2L3.2 7.8l1.4-2.4 2 .8 1.6-.9z"/>
  </symbol>
</svg>

<!-- app logo concepts -->
<div class="app-tile app-tile--purple tile-one">ZoVEX</div>
<div class="app-tile app-tile--purple tile-two">ZoVEX</div>
<div class="app-tile app-tile--ocean tile-three">ZoVEX</div>

<!-- home screen: cards + tab bar -->
<section class="screen screen--cards">
  <div class="status-bar">
    <div class="status-left">●●●●● Carrier</div>
    <div class="status-time">9:41 AM</div>
    <div class="status-right">100% <div class="battery"><span></span></div></div>
  </div>
  <header class="app-header">
    <svg class="header-icon header-icon--left"><use href="#icon-steps"/></svg>
    <h1 class="app-title">ZoVEX</h1>
    <svg class="header-icon header-icon--right"><use href="#icon-gear"/></svg>
  </header>
  <div class="content-card card-top"></div>
  <div class="content-card card-bottom"></div>
  <nav class="tab-bar">
    <div class="tab tab--active"><svg><use href="#icon-info"/></svg>Info</div>
    <div class="tab"><svg><use href="#icon-plan"/></svg>Plan</div>
    <div class="tab"><svg><use href="#icon-sync"/></svg>Sharing</div>
    <div class="tab"><svg><use href="#icon-tip"/></svg>Tip</div>
  </nav>
</section>

<!-- home screen: bubbles -->
<section class="screen screen--bubbles">
  <div class="status-bar">
    <div class="status-left">●●●●● Carrier</div>
    <div class="status-time">9:41 AM</div>
    <div class="status-right">100% <div class="battery"><span></span></div></div>
  </div>
  <header class="app-header">
    <svg class="header-icon header-icon--left"><use href="#icon-steps"/></svg>
    <h1 class="app-title">ZoVEX</h1>
    <svg class="header-icon header-icon--right"><use href="#icon-gear"/></svg>
  </header>
  <div class="bubble" style="left:32px;top:95px"><svg><use href="#icon-info"/></svg></div>
  <span class="bubble-label" style="left:146px;top:131px">Info</span>
  <div class="bubble" style="left:186px;top:208px"><svg><use href="#icon-plan"/></svg></div>
  <span class="bubble-label" style="left:128px;top:245px">Plan</span>
  <div class="bubble" style="left:32px;top:313px"><svg><use href="#icon-sync"/></svg></div>
  <span class="bubble-label" style="left:150px;top:346px">Sharing</span>
  <div class="bubble" style="left:186px;top:428px"><svg><use href="#icon-tip"/></svg></div>
  <span class="bubble-label" style="left:142px;top:468px">Tip</span>
</section>

<!-- home screen: colour rows -->
<section class="screen screen--rows">
  <div class="status-bar">
    <div class="status-left">●●●●● Carrier</div>
    <div class="status-time">9:41 AM</div>
    <div class="status-right">100% <div class="battery"><span></span></div></div>
  </div>
  <header class="app-header">
    <svg class="header-icon header-icon--left"><use href="#icon-steps"/></svg>
    <h1 class="app-title">ZoVEX</h1>
    <svg class="header-icon header-icon--right"><use href="#icon-gear"/></svg>
  </header>
  <div class="nav-row row-info"><svg><use href="#icon-info"/></svg><span>Info</span></div>
  <div class="nav-row row-plan"><svg><use href="#icon-plan"/></svg><span>Plan</span></div>
  <div class="nav-row row-share"><svg><use href="#icon-sync"/></svg><span>Sharing</span></div>
  <div class="nav-row row-tip"><svg><use href="#icon-tip"/></svg><span>Tip</span></div>
</section>

</body>
</html>
```